Tallowmere Consulting Group Business Card Design

We have the logo we just need someone to design a modern business card design.

Name: Leopold Ganzhurt
Phone: 3052918364
Mobile: 9178402297
Web:www.tallowmereconsulting.com
email: lganzhurt@tallowmereconsulting.com
Company: Tallowmere Consulting Group
Title: CEO

Address: 718 Quenby Ave, Miami, Florida 33187

Target Market(s)

companies over 100 employees

Industry/Entity Type

Business

```html
<!DOCTYPE html>
<html lang="en">
<head>
<meta charset="utf-8">
<title>Tallowmere Consulting Group – Business Card</title>
<link href="https://fonts.googleapis.com/css2?family=Nunito+Sans:wght@400;600;700;800&display=swap" rel="stylesheet">
<style>
  :root {
    --brand-blue: #2b9de3;
    --brand-blue-deep: #1a7fc8;
    --ink: #2b2b2b;
    --ink-soft: #555a5f;
    --band-grey: #4a4d52;
    --paper: #ffffff;
    --backdrop: #e9eaec;
  }
  * { box-sizing: border-box; margin: 0; padding: 0; }
  html, body {
    width: 1200px; height: 913px; overflow: hidden;
    background: var(--backdrop);
    font-family: "Nunito Sans", Arial, sans-serif;
  }
  .sheet {
    position: relative; width: 1200px; height: 913px;
    display: flex; align-items: center; justify-content: center; gap: 40px;
  }
  .card {
    position: relative; width: 540px; height: 309px;
    background: var(--paper);
    box-shadow: 0 6px 18px rgba(0,0,0,.12);
    overflow: hidden;
  }
  /* front */
  .card--front { display: flex; align-items: center; justify-content: center; }
  .brand { display: flex; align-items: center; gap: 16px; }
  .brand__dot {
    width: 64px; height: 64px; border-radius: 50%;
    background: var(--brand-blue); flex: none;
  }
  .brand__name {
    color: var(--ink); font-weight: 800; font-size: 26px;
    line-height: 1.05; text-transform: uppercase; letter-spacing: .5px;
    width: 230px;
  }
  /* back */
  .card__bands { position: absolute; inset: 0; width: 100%; height: 100%; }
  .contact {
    position: absolute; left: 30px; top: 88px; width: 300px;
    text-align: right;
  }
  .contact__name { color: var(--brand-blue); font-weight: 700; font-size: 17px; line-height: 1.1; }
  .contact__title { color: var(--ink-soft); font-size: 11px; margin-bottom: 8px; }
  .contact__list { list-style: none; }
  .contact__item {
    display: flex; justify-content: flex-end; align-items: center; gap: 10px;
    color: var(--ink); font-size: 11.5px; line-height: 19px;
  }
  .contact__icon { width: 12px; height: 12px; flex: none; }
  .divider {
    position: absolute; left: 350px; top: 86px; width: 1px; height: 140px;
    background: var(--brand-blue);
  }
  .card--back .brand {
    position: absolute; left: 372px; top: 118px; gap: 10px;
    flex-direction: column; align-items: flex-start;
  }
  .card--back .brand__dot { width: 44px; height: 44px; }
  .card--back .brand__name { font-size: 16px; width: 150px; }
</style>
</head>
<body>
<main class="sheet">

  <section class="card card--front" aria-label="Card front">
    <div class="brand">
      <span class="brand__dot"></span>
      <span class="brand__name">Tallowmere Consulting Group</span>
    </div>
  </section>

  <section class="card card--back" aria-label="Card back">
    <svg class="card__bands" viewBox="0 0 540 309" preserveAspectRatio="none" aria-hidden="true">
      <path d="M300 0 L540 0 L540 22 Q430 10 300 0 Z" fill="var(--band-grey)"/>
      <path d="M420 0 L540 0 L540 10 Q480 4 420 0 Z" fill="var(--brand-blue)"/>
      <path d="M0 309 L0 250 Q200 330 540 190 L540 309 Z" fill="var(--brand-blue)"/>
      <path d="M0 309 L0 272 Q230 340 540 225 L540 309 Z" fill="#111316"/>
      <path d="M0 309 L0 292 Q260 345 540 258 L540 309 Z" fill="var(--brand-blue-deep)"/>
    </svg>

    <div class="contact">
      <p class="contact__name">Leopold Ganzhurt</p>
      <p class="contact__title">CEO</p>
      <ul class="contact__list">
        <li class="contact__item">718 Quenby Ave, Miami, Florida 33187
          <svg class="contact__icon" viewBox="0 0 12 12"><path d="M6 0.5a3.6 3.6 0 0 0-3.6 3.6C2.4 7 6 11.5 6 11.5S9.6 7 9.6 4.1A3.6 3.6 0 0 0 6 .5Zm0 5a1.4 1.4 0 1 1 0-2.8 1.4 1.4 0 0 1 0 2.8Z" fill="var(--brand-blue)"/></svg>
        </li>
        <li class="contact__item">3052918364
          <svg class="contact__icon" viewBox="0 0 12 12"><path d="M2.5 1h2l1 2.6-1.3.9a6.5 6.5 0 0 0 3.3 3.3l.9-1.3 2.6 1v2A1.5 1.5 0 0 1 9.5 11 8.5 8.5 0 0 1 1 2.5 1.5 1.5 0 0 1 2.5 1Z" fill="var(--brand-blue)"/></svg>
        </li>
        <li class="contact__item">9178402297
          <svg class="contact__icon" viewBox="0 0 12 12"><rect x="3" y="0.5" width="6" height="11" rx="1.2" fill="none" stroke="var(--brand-blue)" stroke-width="1.2"/><circle cx="6" cy="9.6" r=".7" fill="var(--brand-blue)"/></svg>
        </li>
        <li class="contact__item">www.tallowmereconsulting.com
          <svg class="contact__icon" viewBox="0 0 12 12"><g fill="none" stroke="var(--brand-blue)" stroke-width="1"><circle cx="6" cy="6" r="5"/><ellipse cx="6" cy="6" rx="2.2" ry="5"/><path d="M1 6h10"/></g></svg>
        </li>
        <li class="contact__item">lganzhurt@tallowmereconsulting.com
          <svg class="contact__icon" viewBox="0 0 12 12"><rect x="0.8" y="2.3" width="10.4" height="7.4" rx="1" fill="var(--brand-blue)"/><path d="M1.2 3l4.8 3.6L10.8 3" fill="none" stroke="#fff" stroke-width="1"/></svg>
        </li>
      </ul>
    </div>

    <span class="divider" aria-hidden="true"></span>

    <div class="brand">
      <span class="brand__dot"></span>
      <span class="brand__name">Tallowmere Consulting Group</span>
    </div>
  </section>

</main>
</body>
</html>
```